Brantley Advisory Group provides support for renewable energy projects to utilities and suppliers

I need a professional looking business card that is both simple and elegant and unique. My clients are mostly large organizations not individuals. I am a consultant with my own company that is small but would like to give clients the impression I am larger. Smart grid, fiber optics, software, field hardware, distribution automation, substation automation, operations, energy storage/batteries, microgrids, customer service, strategy/roadmaps, conservation, Automated Metering Infrastruture (AMI or smart meters) are all areas of focus.

Target Market(s)

Utilities, suppliers, governmental agencies involved in energy. All types of energy especially natural gas and electrical. Especially renewable energy or green projects.

Contact Information for Business Card

Name - Mark Brantley Cell Phone - 425.318.2746 Email - mbrantley@brantleyag-example.com
Company - Brantley Advisory Group (logo) Title - Principal

Font styles to use
Serif
Sans Serif

Colors

Designer to choose colors to be used in the design.

Requirements
Must have
• Simple and professional and powerful.
• Unique/creative design.
Nice to have
• Utilize color scheme to accent logo colors. Maybe some geometric pattern on edge of card with color.
Should not have
• Busy, complicated, traditional

```html
<!DOCTYPE html>
<html lang="en">
<head>
<meta charset="utf-8">
<title>Brantley Advisory Group — Business Card</title>
<link rel="stylesheet" href="https://fonts.googleapis.com/css2?family=Lato:wght@400;900&display=swap">
<style>
  :root {
    --page-bg: #e9eaee;
    --brand-navy: #2b3592;
    --brand-green: #5a9140;
    --card-white: #ffffff;
    --text-grey: #4a4a4a;
    --muted-grey: #6b6b6b;
  }
  * { margin: 0; padding: 0; box-sizing: border-box; }
  html, body { width: 1200px; height: 900px; overflow: hidden; }
  body {
    background: var(--page-bg);
    font-family: "Lato", sans-serif;
    position: relative;
  }
  .card {
    position: absolute;
    width: 700px;
    height: 400px;
    border-radius: 22px;
    box-shadow: 0 10px 28px rgba(0,0,0,0.18);
    overflow: hidden;
  }
  /* Back side */
  .card-back {
    left: 60px; top: 40px;
    background: var(--brand-navy);
    color: var(--card-white);
  }
  .card-back .wordmark {
    position: absolute;
    left: 0; right: 0; top: 130px;
    display: flex; justify-content: center; align-items: center; gap: 18px;
  }
  .wordmark-square {
    width: 34px; height: 34px;
    border: 4px solid currentColor;
    border-radius: 6px;
  }
  .wordmark-name {
    font-weight: 900;
    font-size: 40px;
    line-height: 1.05;
    letter-spacing: 0.5px;
  }
  .card-back .back-url {
    position: absolute;
    left: 0; right: 0; bottom: 60px;
    text-align: center;
    font-size: 15px;
    letter-spacing: 6px;
  }
  /* Front side */
  .card-front {
    left: 440px; top: 470px;
    background: var(--card-white);
  }
  .card-front .wordmark {
    position: absolute;
    left: 48px; top: 50px;
    display: flex; align-items: center; gap: 16px;
    color: var(--brand-navy);
  }
  .card-front .wordmark-name { font-size: 34px; }
  .contact-block {
    position: absolute;
    left: 48px; bottom: 42px;
    color: var(--text-grey);
    font-size: 15px;
    line-height: 1.55;
  }
  .address { margin-bottom: 10px; }
  .contact-row { display: flex; align-items: center; gap: 12px; }
  .contact-icon { width: 16px; height: 16px; flex: none; }
  .url-accent { color: var(--brand-navy); }
  .person {
    position: absolute;
    right: 52px; top: 160px;
    text-align: right;
  }
  .person-name {
    font-weight: 900;
    font-size: 36px;
    color: var(--brand-navy);
    letter-spacing: -0.5px;
  }
  .person-title {
    font-size: 16px;
    color: var(--muted-grey);
    letter-spacing: 3px;
    margin-top: 2px;
  }
</style>
</head>
<body>

<section class="card card-back" aria-label="Card back">
  <div class="wordmark">
    <span class="wordmark-square" aria-hidden="true"></span>
    <span class="wordmark-name">Brantley Advisory Group</span>
  </div>
  <p class="back-url">www.brantleyag-example.com</p>
</section>

<section class="card card-front" aria-label="Card front">
  <div class="wordmark">
    <span class="wordmark-square" aria-hidden="true"></span>
    <span class="wordmark-name">Brantley Advisory Group</span>
  </div>

  <div class="person">
    <p class="person-name">Mark Brantley</p>
    <p class="person-title">Principal</p>
  </div>

  <div class="contact-block">
    <p class="address">1234 First Line Address<br>5678 Second Line Address</p>
    <p class="contact-row">
      <svg class="contact-icon" viewBox="0 0 16 16" aria-hidden="true"><path fill="#5a9140" d="M3.6 1.2l2.3 2.6-1.2 1.8c.8 1.9 2.1 3.3 4 4.3l1.8-1.2 2.6 2.3-1.3 2.4C6.5 13.3 2.4 9.3 1.2 3.8z"/></svg>
      425.318.2746
    </p>
    <p class="contact-row">
      <svg class="contact-icon" viewBox="0 0 16 16" aria-hidden="true"><rect x="1" y="3" width="14" height="10" rx="1" fill="#5a9140"/><path d="M1.5 3.5L8 9l6.5-5.5" fill="none" stroke="#fff" stroke-width="1.2"/></svg>
      mbrantley@brantleyag-example.com
    </p>
    <p class="contact-row">
      <svg class="contact-icon" viewBox="0 0 16 16" aria-hidden="true"><g fill="none" stroke="#5a9140" stroke-width="1.3"><circle cx="8" cy="8" r="6.5"/><ellipse cx="8" cy="8" rx="2.8" ry="6.5"/><path d="M1.5 8h13M2.5 4.8h11M2.5 11.2h11"/></g></svg>
      <span>www.<span class="url-accent">brantleyag-example</span>.com</span>
    </p>
  </div>
</section>

</body>
</html>
```